Bright Ledger Hosting Workdeck 720 Flyer

We have a requirement to start sending out product / service information to our clients and resellers. Currently this type of communication is only via the LinkedIn/ Twitter / Blog articles and we want to change this to an email campaign with pdf and the ability to print and send by post.

We have a powerpoint draft of the flyer that will be a pdf and potentially a handout but it looks like a powerpoint and not something classy. I have included the powerpoint and four images along with our current logo (although this may change soon)

Target Market(s)

MSP Resellers, Direct Clients

Industry/Entity Type

It Service

Colors

Designer to choose colors to be used in the design.

Requirements
Must have
• The flow and feel from our website and social media so that it has our identity. Our core colors are on the website. Anything new must be complementary.
• Modern and technical feel
Nice to have
• Sense of security and trust. Our new strap line is to be "Simple, Safe, Secure" so some experimentation on this would be nice
Should not have
• nothing of note

```html
<!DOCTYPE html>
<html lang="en">
<head>
<meta charset="utf-8">
<title>Understand the Risks – Bright Ledger Hosting</title>
<link href="https://fonts.googleapis.com/css2?family=Open+Sans:wght@300;400;600;700&display=swap" rel="stylesheet">
<style>
  :root {
    --paper: #ffffff;
    --kicker: #8a8a8a;
    --title: #c9c5ae;
    --body: #707070;
    --body-strong: #6a6a6a;
    --accent-red: #c0392b;
    --brand-ink: #3a3a3a;
    --brand-blue: #3a8fd0;
    --scene-sky: #e7e1c9;
    --scene-mid: #cdbf9c;
    --scene-ground: #b9a98a;
  }
  * { margin: 0; padding: 0; box-sizing: border-box; }
  html, body { width: 855px; height: 1200px; overflow: hidden; background: var(--paper); }
  body { font-family: "Open Sans", Arial, sans-serif; color: var(--body); }
  .flyer { position: relative; width: 855px; height: 1200px; overflow: hidden; }

  .kicker {
    position: absolute; top: 30px; right: 32px;
    font-size: 17px; font-weight: 300; letter-spacing: 0.3px;
    color: var(--kicker); text-transform: uppercase;
  }
  .headline {
    position: absolute; top: 80px; left: 46px;
    font-size: 63px; font-weight: 300; line-height: 1;
    color: var(--title); letter-spacing: 0.5px; white-space: nowrap;
  }
  .hero {
    position: absolute; top: 155px; left: 0; width: 855px; height: 422px;
    background: linear-gradient(180deg, var(--scene-sky) 0%, #ddd3b6 45%, var(--scene-mid) 62%, var(--scene-ground) 100%);
  }

  .copy { position: absolute; left: 50px; width: 770px; font-size: 17.5px; line-height: 21.5px; }
  .intro { top: 606px; }
  .lead-in { top: 720px; }
  .risk-list { position: absolute; top: 766px; left: 50px; list-style: none; }
  .risk-list li {
    position: relative; padding-left: 24px;
    font-size: 17.5px; line-height: 22.2px; font-weight: 700; color: var(--body-strong);
  }
  .risk-list li::before {
    content: ""; position: absolute; left: 2px; top: 6px;
    border-left: 9px solid var(--accent-red);
    border-top: 5px solid transparent; border-bottom: 5px solid transparent;
  }
  .limits { top: 920px; }
  .closing { top: 1028px; }

  .brand {
    position: absolute; left: 52px; top: 1130px;
    display: flex; align-items: center; gap: 12px;
  }
  .brand-dot { width: 30px; height: 30px; border-radius: 50%; background: var(--brand-blue); }
  .brand-name { font-size: 20px; font-weight: 600; color: var(--brand-ink); letter-spacing: 0.2px; text-transform: uppercase; }
</style>
</head>
<body>
  <main class="flyer">
    <p class="kicker">The reasons why you need to backup Workdeck 720</p>
    <h1 class="headline">UNDERSTAND THE RISKS</h1>
    <div class="hero" role="img" aria-label="Sepia photograph of a child in a helmet and goggles peeking out of a circus cannon on an empty desert road with mountains behind"></div>

    <p class="copy intro">Corvane ensure that your applications and data are available to you but your Workdeck 720 data is still vulnerable to some significant risks. There are many studies that report about how data loss can be pretty devastating for a company but the time lost in attempting data recovery can be equally damaging.</p>

    <p class="copy lead-in">Cloud-based data is vulnerable to:</p>

    <ul class="risk-list">
      <li>Malware damage and ransomware attacks</li>
      <li>Accidental or malicious deletion</li>
      <li>Retention policy gaps and confusion</li>
      <li>Cancelled user licenses causing data loss</li>
      <li>Intentional or accidental data overwrites</li>
      <li>Lost time when restoring data</li>
    </ul>

    <p class="copy limits">Corvane does provide some restore abilities but they are very primitive and come with some pretty important limits that companies are unaware of. There is a study by Corvane that state that data compromises can go undetected or about 140 days but the Recycle Bin only keeps the data for 93 days.</p>

    <p class="copy closing">That by itself should be a good enough reason to consider a backup service to protect your business.</p>

    <div class="brand">
      <span class="brand-dot"></span>
      <span class="brand-name">Bright Ledger Hosting</span>
    </div>
  </main>
</body>
</html>
```